3 page designs for our Travel Company!!

Hi there!
We need 3 page designs to add to our travel website. We have include the PSD files of relevant web pages for you to use. We would like the new designs to fit in with the pages we already have designed please (colours, layout & style)
We require the following pages:
1. Hotel Search Page
2. Hotel Page
- For these pages, we are looking for an aesthetic design layout that fits in line with the layout of the pages we have designed. (PSD files 'Tour Page' & 'Tour Search Pages')
- We want to see imaginative ways of arranging the content in pleasant and 'easy to read' layouts.
3. Mobile View Page
- This is simply the design layout for the 'Mobile View'.
- We want you to illustrate how the drop down menus will work.
- Simplicity is key here. We want the menus to be easy to understand
- The 'Discover Cayman' menu is the only menu with multiple sub categories (You can see this in the PSD file named 'Drop Down Menu')
You can find our support documents here at https://www.filquarry.net/sh/7k21mdqzhrtt93p/QWxeLmPNvKrtaZu8fGh02bYRq?dl=0
Please feel free to get imaginative with unique ways these pages can be played out!
Thank you!

```html
<!DOCTYPE html>
<html lang="en">
<head>
<meta charset="utf-8">
<title>IsleRoute – Hotel Search</title>
<link href="https://fonts.googleapis.com/css2?family=Montserrat:wght@500;600;700;800&family=Lato:wght@400;700&display=swap" rel="stylesheet">
<style>
:root{
  --blue:#1f6fd1;
  --green:#7dbb2c;
  --green-dark:#5f9a1a;
  --red:#e0141b;
  --text:#333;
  --muted:#555;
  --line:#d9d9d9;
  --panel:#f6f6f6;
  --footer:#6c6b6b;
  --white:#fff;
}
*{box-sizing:border-box;margin:0;padding:0}
html,body{width:759px;height:1200px;overflow:hidden;background:#fff}
body{position:relative;font-family:'Lato',sans-serif;color:var(--text)}
.abs{position:absolute}
svg{display:block}

/* header */
.brand{left:91px;top:15px;display:flex;align-items:center;gap:6px;font-family:'Montserrat',sans-serif;font-weight:700;font-size:26px;color:var(--blue);letter-spacing:-.3px}
.brand-mark{width:30px;height:30px;background:var(--green);border-radius:3px}
.header-tools{left:572px;top:22px;display:flex;align-items:center;gap:8px}
.login{font-family:'Montserrat',sans-serif;font-weight:600;font-size:11px;color:var(--green);margin-right:4px}
.nav{left:0;top:59px;width:759px;height:35px;border-top:1px solid #e6e6e6}
.nav-item{top:69px;display:flex;align-items:center;gap:6px;font-family:'Montserrat',sans-serif;font-weight:600;font-size:10px;color:#555}
.nav-item.active{color:var(--green)}
.nav-icon{width:16px;height:16px}
.dest-select{left:537px;top:66px;width:130px;height:22px;background:#f0f0f0;font-size:8px;color:#888;padding:6px 8px}
.caret{position:absolute;right:8px;top:9px;border-left:3px solid transparent;border-right:3px solid transparent;border-top:4px solid #555}

/* hero */
.hero{left:0;top:94px;width:759px;height:270px;background:linear-gradient(180deg,#7fb4e2 0%,#a9cbe6 28%,#3aa6c9 45%,#c8b8a0 70%,#a89070 100%)}
.hero-title{left:0;top:200px;width:759px;text-align:center;font-family:'Montserrat',sans-serif;font-weight:800;font-size:46px;color:var(--white);letter-spacing:1px;text-shadow:0 2px 6px rgba(0,0,0,.25)}

/* search bar */
.field{top:390px;height:23px;border:1px solid var(--line);background:#fff;font-size:8px;color:#555;display:flex;align-items:center}
.field .ph{margin-left:6px}
.date{color:var(--blue);margin-left:4px}
.book{left:590px;top:389px;width:78px;height:24px;background:var(--green);border-bottom:2px solid var(--green-dark);color:#fff;font-weight:700;font-size:8px;display:flex;align-items:center;justify-content:center;border-radius:2px}

/* results panel */
.results{left:91px;top:421px;width:577px;height:556px;border:1px solid #e2e2e2;box-shadow:0 1px 4px rgba(0,0,0,.08);background:#fff}
.filter-bar{left:91px;top:421px;width:577px;height:38px;border-bottom:1px solid #e6e6e6}
.filter-label{left:124px;top:435px;font-weight:700;font-size:9px;color:#333}
.view-btn{top:429px;height:23px;border-radius:3px;font-weight:700;font-size:8px;color:#222;display:flex;align-items:center;justify-content:center;gap:6px;background:#fff}
.view-list{left:474px;width:78px;border:1px solid var(--green)}
.view-map{left:555px;width:78px;border:1px solid var(--blue)}

/* sidebar */
.sidebar{left:100px;top:471px;width:196px;height:478px;background:#fff;box-shadow:0 0 6px rgba(0,0,0,.1)}
.side-head{left:120px;display:flex;align-items:center;gap:6px;font-size:11px;color:var(--blue)}
.side-head .ico{width:11px;height:11px}
.sort-select{left:120px;top:507px;width:157px;height:20px;border:1px solid #cfcfcf;font-size:8px;color:#444;padding:5px 17px}
.divider{left:120px;width:157px;height:1px;background:var(--line)}
.opt{left:123px;width:154px;display:flex;align-items:center;font-size:7.5px;color:#555}
.radio{width:7px;height:7px;border:1.3px solid var(--blue);border-radius:50%;margin-right:7px}
.radio.on{background:radial-gradient(var(--blue) 45%,#fff 55%)}
.opt .count{margin-left:auto;color:var(--blue);font-weight:700}
.budget{left:138px;top:640px;font-size:8px;color:#444}
.slider{left:120px;top:660px;width:157px;height:2px;background:#d6d6d6}
.slider-fill{left:120px;top:660px;width:37px;height:2px;background:var(--green)}
.slider-knob{left:153px;top:656px;width:9px;height:9px;border-radius:50%;background:#fff;border:1.5px solid var(--green)}

/* hotel cards */
.card{left:308px;width:346px;height:113px;border:1px solid #e2e2e2;background:#fff}
.card-photo{position:absolute;left:10px;top:8px;width:88px;height:96px}
.card-title{position:absolute;left:107px;top:12px;font-size:12px;color:var(--blue);white-space:nowrap}
.card-loc{position:absolute;left:107px;top:33px;display:flex;align-items:center;gap:5px;font-size:7.5px;color:#555}
.card-loc b{color:#222;font-size:8px}
.card-amen{position:absolute;left:107px;top:48px;font-size:7.5px;color:#555;white-space:nowrap}
.card-price{position:absolute;left:107px;top:68px;font-size:13px;font-weight:700;color:var(--green)}
.card-left{position:absolute;left:107px;top:85px;font-size:7.5px;font-weight:700;color:var(--red)}
.choose{position:absolute;left:271px;top:67px;width:63px;height:24px;background:var(--green);border-bottom:2px solid var(--green-dark);border-radius:2px;color:#fff;font-weight:700;font-size:7.5px;display:flex;align-items:center;justify-content:center}

/* footer */
.footer{left:0;top:999px;width:759px;height:201px;background:var(--footer);border-top:3px solid var(--green)}
.f-head{top:1031px;font-size:13px;font-weight:700;color:#fff;letter-spacing:.2px}
.f-links{top:1055px;list-style:none;font-size:8.5px;color:#f2f2f2;line-height:16.2px}
.email{left:446px;top:1055px;width:146px;height:22px;background:#fff;font-size:8px;color:#444;padding:7px 11px}
.signup{left:592px;top:1055px;width:62px;height:22px;background:var(--green);color:#fff;font-weight:700;font-size:9px;display:flex;align-items:center;justify-content:center}
.f-note{left:446px;top:1089px;font-size:11px;font-weight:700;color:#fff}
.social{top:1116px;width:20px;height:20px;border-radius:50%}
.f-rule{left:83px;top:1161px;width:592px;height:1px;background:#8a8a8a}
.copy{left:0;top:1178px;width:759px;text-align:center;font-size:7.5px;color:#f2f2f2}
</style>
</head>
<body>

<!-- header -->
<div class="abs brand"><span class="brand-mark"></span>IsleRoute</div>
<div class="abs header-tools">
  <span class="login">Log in</span>
  <svg width="14" height="14" viewBox="0 0 14 14" fill="#7dbb2c"><rect x="0" y="0" width="4" height="4"/><rect x="5" y="0" width="4" height="4"/><rect x="10" y="0" width="4" height="4"/><rect x="0" y="5" width="4" height="4"/><rect x="5" y="5" width="4" height="4"/><rect x="10" y="5" width="4" height="4"/><rect x="0" y="10" width="4" height="4"/><rect x="5" y="10" width="4" height="4"/><rect x="10" y="10" width="4" height="4"/></svg>
  <svg width="16" height="16" viewBox="0 0 16 16"><circle cx="8" cy="8" r="7" fill="none" stroke="#7dbb2c" stroke-width="1.4"/><path d="M6 6.3a2 2 0 1 1 2.6 1.9c-.5.2-.6.5-.6 1V10" fill="none" stroke="#7dbb2c" stroke-width="1.4"/><circle cx="8" cy="12" r=".9" fill="#7dbb2c"/></svg>
  <svg width="16" height="16" viewBox="0 0 16 16"><circle cx="6.5" cy="6.5" r="5" fill="none" stroke="#7dbb2c" stroke-width="1.6"/><path d="M10.2 10.2L15 15" stroke="#7dbb2c" stroke-width="2"/></svg>
</div>

<div class="abs nav"></div>
<div class="abs nav-item" style="left:91px"><svg class="nav-icon" viewBox="0 0 16 16"><path d="M8 15V6M8 6C6 3 3 3 2 4M8 6c2-3 5-3 6-2M8 6C7 3 8 1 9 1" stroke="#1f6fd1" stroke-width="1.4" fill="none"/><path d="M2 15h12" stroke="#1f6fd1" stroke-width="1.4"/></svg>Discover Cayman</div>
<div class="abs nav-item" style="left:218px"><svg class="nav-icon" viewBox="0 0 16 16"><rect x="1" y="3" width="14" height="12" rx="1" fill="none" stroke="#1f6fd1" stroke-width="1.4"/><path d="M1 6h14M4 1v3M12 1v3" stroke="#1f6fd1" stroke-width="1.4"/><g fill="#1f6fd1"><rect x="3" y="8" width="2" height="2"/><rect x="7" y="8" width="2" height="2"/><rect x="11" y="8" width="2" height="2"/><rect x="3" y="11" width="2" height="2"/><rect x="7" y="11" width="2" height="2"/></g></svg>Build A Trip</div>
<div class="abs nav-item" style="left:313px"><svg class="nav-icon" viewBox="0 0 16 16"><circle cx="10" cy="2.5" r="1.6" fill="#1f6fd1"/><path d="M10 5l-2 5-4 1M8 10l2 5M9 6l4 2" stroke="#1f6fd1" stroke-width="1.6" fill="none"/></svg>Activities</div>
<div class="abs nav-item active" style="left:396px"><svg class="nav-icon" viewBox="0 0 16 16"><path d="M1 6l7-4 7 4" fill="none" stroke="#7dbb2c" stroke-width="1.6"/><rect x="2" y="7" width="12" height="8" fill="#1f6fd1"/><rect x="4" y="10" width="3" height="5" fill="#fff"/><rect x="9" y="9" width="3" height="2" fill="#fff"/></svg><span style="margin-left:8px">Accomodations</span></div>
<div class="abs dest-select">Search Destinations<span class="caret"></span></div>

<!-- hero -->
<div class="abs hero" role="img" aria-label="Photo of a resort infinity pool with white sun loungers, palm trees and the sea behind"></div>
<div class="abs hero-title">HOTEL SEARCH</div>

<!-- search bar -->
<div class="abs field" style="left:91px;width:163px">
  <svg style="margin-left:8px" width="9" height="9" viewBox="0 0 10 10"><circle cx="4" cy="4" r="3.2" fill="none" stroke="#7dbb2c" stroke-width="1.2"/><path d="M6.5 6.5L9.5 9.5" stroke="#7dbb2c" stroke-width="1.3"/></svg>
  <span class="ph" style="margin-left:12px">Search Hotel...</span>
</div>
<div class="abs field" style="left:260px;width:246px">
  <span style="margin-left:10px">Check in</span><span class="date">dd/mm/yyy</span>
  <svg style="margin-left:6px" width="8" height="8" viewBox="0 0 8 8"><rect x=".5" y="1" width="7" height="6.5" fill="none" stroke="#7dbb2c"/><path d="M.5 3h7" stroke="#7dbb2c"/></svg>
  <span style="width:1px;height:23px;background:#e2e2e2;margin:0 8px"></span>
  <span>Check out</span><span class="date">dd/mm/yyy</span>
  <svg style="margin-left:6px" width="8" height="8" viewBox="0 0 8 8"><rect x=".5" y="1" width="7" height="6.5" fill="none" stroke="#7dbb2c"/><path d="M.5 3h7" stroke="#7dbb2c"/></svg>
  <span class="caret" style="top:10px"></span>
</div>
<div class="abs field" style="left:510px;width:75px">
  <svg style="margin-left:11px" width="8" height="8" viewBox="0 0 8 8"><circle cx="2.5" cy="2.5" r="2" fill="#7dbb2c"/><path d="M3.5 3.5L7.5 7.5" stroke="#7dbb2c" stroke-width="1.3"/></svg>
  <span style="margin-left:8px">Room</span><span class="caret" style="top:10px"></span>
</div>
<div class="abs book">BOOK NOW</div>

<!-- results panel -->
<div class="abs results"></div>
<div class="abs filter-bar"></div>
<svg class="abs" style="left:100px;top:434px" width="12" height="12" viewBox="0 0 12 12"><path d="M2 0v12M6 0v12M10 0v12" stroke="#1f6fd1" stroke-width="1"/><circle cx="2" cy="4" r="1.5" fill="#fff" stroke="#7dbb2c"/><circle cx="6" cy="8" r="1.5" fill="#fff" stroke="#7dbb2c"/><circle cx="10" cy="3" r="1.5" fill="#fff" stroke="#7dbb2c"/></svg>
<div class="abs filter-label">FILTER</div>
<div class="abs view-btn view-list"><svg width="10" height="8" viewBox="0 0 10 8" fill="#7dbb2c"><rect width="2" height="2"/><rect x="3" width="7" height="2"/><rect y="3" width="2" height="2"/><rect x="3" y="3" width="7" height="2"/><rect y="6" width="2" height="2"/><rect x="3" y="6" width="7" height="2"/></svg>LIST VIEW</div>
<div class="abs view-btn view-map"><svg width="7" height="10" viewBox="0 0 7 10"><path d="M3.5 10S0 5.6 0 3.5a3.5 3.5 0 0 1 7 0C7 5.6 3.5 10 3.5 10z" fill="#1f6fd1"/><circle cx="3.5" cy="3.5" r="1.3" fill="#fff"/></svg>MAP VIEW</div>

<!-- sidebar -->
<div class="abs sidebar"></div>

<div class="abs side-head" style="top:485px"><svg class="ico" viewBox="0 0 12 12"><path d="M2 0v11M0 9l2 2 2-2" stroke="#7dbb2c" stroke-width="1.2" fill="none"/><path d="M6 2h6M6 5h5M6 8h4M6 11h6" stroke="#7dbb2c" stroke-width="1.2"/></svg>Sort by</div>
<div class="abs sort-select">Recommended<span class="caret" style="top:8px"></span></div>
<div class="abs divider" style="top:537px"></div>

<div class="abs side-head" style="top:546px"><svg class="ico" viewBox="0 0 12 12"><path d="M1 2v9M1 7h10v4M3 6V4h3v2" stroke="#7dbb2c" stroke-width="1.6" fill="none"/></svg>Amenities</div>
<div class="abs opt" style="top:564px"><span class="radio"></span>Free Internet Access<span class="count">19</span></div>
<div class="abs opt" style="top:578px"><span class="radio on"></span>Free Breakfast<span class="count" style="margin-right:6px">1</span></div>
<div class="abs opt" style="top:592px"><span class="radio"></span>Free Parking<span class="count">19</span></div>
<div class="abs divider" style="top:614px"></div>

<div class="abs side-head" style="top:622px"><svg class="ico" viewBox="0 0 12 12"><circle cx="4" cy="7.5" r="3.5" fill="#7dbb2c"/><path d="M8 4h4M8 7h4M8 10h4" stroke="#7dbb2c" stroke-width="1.2"/></svg>Set Your Budget</div>
<div class="abs budget">$0 to $500</div>
<div class="abs slider"></div>
<div class="abs slider-fill"></div>
<div class="abs slider-knob"></div>
<div class="abs divider" style="top:679px"></div>

<div class="abs side-head" style="top:687px"><svg class="ico" viewBox="0 0 12 12"><path d="M0 6L6 1l6 5" stroke="#7dbb2c" stroke-width="1.5" fill="none"/><path d="M2 6v6h8V6L6 3z" fill="#7dbb2c"/></svg>Neighborhoods</div>
<div class="abs opt" style="top:706px"><span class="radio"></span>Cayman Brac Island<span class="count">19</span></div>
<div class="abs opt" style="top:720px"><span class="radio on"></span>East End<span class="count" style="margin-right:6px">1</span></div>
<div class="abs opt" style="top:734px"><span class="radio"></span>Seven Mile Beach<span class="count">19</span></div>
<div class="abs divider" style="top:754px"></div>

<div class="abs side-head" style="top:763px"><svg class="ico" viewBox="0 0 12 12"><path d="M0 6L6 1l6 5" stroke="#7dbb2c" stroke-width="1.5" fill="none"/><path d="M2 6v6h8V6L6 3z" fill="#7dbb2c"/></svg>Hotel Star Level</div>
<div class="abs opt" style="top:781px"><span class="radio"></span>5 Star<span class="count">20</span></div>
<div class="abs opt" style="top:795px"><span class="radio on"></span>4 Star<span class="count">12</span></div>
<div class="abs opt" style="top:809px"><span class="radio"></span>3 Star<span class="count">18</span></div>
<div class="abs opt" style="top:823px"><span class="radio"></span>2 Star<span class="count">30</span></div>
<div class="abs opt" style="top:837px"><span class="radio"></span>1 Star<span class="count">14</span></div>

<!-- hotel cards -->
<div class="abs card" style="top:471px">
  <div class="card-photo" role="img" aria-label="Photo of a beach resort pool with thatched umbrellas" style="background:linear-gradient(180deg,#4f86c0 0%,#9cc0dc 45%,#c9b48f 55%,#49b6e6 70%,#2d9bd8 100%)"></div>
  <div class="card-title">Palm Harbor Resort Grand Cayman</div>
  <div class="card-loc">Seven Mile Beach <svg width="7" height="10" viewBox="0 0 7 10"><path d="M3.5 10S0 5.6 0 3.5a3.5 3.5 0 0 1 7 0C7 5.6 3.5 10 3.5 10z" fill="#1f6fd1"/><circle cx="3.5" cy="3.5" r="1.3" fill="#fff"/></svg><b>MAP VIEW</b></div>
  <div class="card-amen">Free Parking, Free Internet Access, Swimming Pool</div>
  <div class="card-price">$144</div>
  <div class="card-left">Only 1 Room Left</div>
  <div class="choose">CHOOSE</div>
</div>

<div class="abs card" style="top:593px">
  <div class="card-photo" role="img" aria-label="Photo of a wooden pier leading to overwater bungalows on turquoise sea" style="background:linear-gradient(180deg,#1f5db8 0%,#5d98d8 35%,#8a6a4e 50%,#3ec0cf 65%,#b0a090 100%)"></div>
  <div class="card-title">Palm Harbor Resort Grand Cayman</div>
  <div class="card-loc">Seven Mile Beach <svg width="7" height="10" viewBox="0 0 7 10"><path d="M3.5 10S0 5.6 0 3.5a3.5 3.5 0 0 1 7 0C7 5.6 3.5 10 3.5 10z" fill="#1f6fd1"/><circle cx="3.5" cy="3.5" r="1.3" fill="#fff"/></svg><b>MAP VIEW</b></div>
  <div class="card-amen">Free Parking, Free Internet Access, Swimming Pool</div>
  <div class="card-price">$144</div>
  <div class="card-left">Only 1 Room Left</div>
  <div class="choose">CHOOSE</div>
</div>

<div class="abs card" style="top:713px">
  <div class="card-photo" role="img" aria-label="Photo of a bright hotel bedroom with a desk and wooden floor" style="background:linear-gradient(180deg,#efe9e1 0%,#e4dccf 50%,#f3f1ec 70%,#a87b4f 100%)"></div>
  <div class="card-title">Palm Harbor Resort Grand Cayman</div>
  <div class="card-loc">Seven Mile Beach <svg width="7" height="10" viewBox="0 0 7 10"><path d="M3.5 10S0 5.6 0 3.5a3.5 3.5 0 0 1 7 0C7 5.6 3.5 10 3.5 10z" fill="#1f6fd1"/><circle cx="3.5" cy="3.5" r="1.3" fill="#fff"/></svg><b>MAP VIEW</b></div>
  <div class="card-amen">Free Parking, Free Internet Access, Swimming Pool</div>
  <div class="card-price">$144</div>
  <div class="card-left">Only 1 Room Left</div>
  <div class="choose">CHOOSE</div>
</div>

<div class="abs card" style="top:835px">
  <div class="card-photo" role="img" aria-label="Photo of a modern hotel room with a white bed and orange throw by large windows" style="background:linear-gradient(180deg,#e9eef0 0%,#cfd8d4 45%,#f4f4f2 65%,#e0642a 80%,#d8d8d8 100%)"></div>
  <div class="card-title">Palm Harbor Resort Grand Cayman</div>
  <div class="card-loc">Seven Mile Beach <svg width="7" height="10" viewBox="0 0 7 10"><path d="M3.5 10S0 5.6 0 3.5a3.5 3.5 0 0 1 7 0C7 5.6 3.5 10 3.5 10z" fill="#1f6fd1"/><circle cx="3.5" cy="3.5" r="1.3" fill="#fff"/></svg><b>MAP VIEW</b></div>
  <div class="card-amen">Free Parking, Free Internet Access, Swimming Pool</div>
  <div class="card-price">$144</div>
  <div class="card-left">Only 1 Room Left</div>
  <div class="choose">CHOOSE</div>
</div>

<!-- footer -->
<div class="abs footer"></div>
<div class="abs f-head" style="left:91px">COMPANY</div>
<ul class="abs f-links" style="left:91px"><li>About us</li><li>How it works ?</li><li>Our investors</li><li>Contact us</li><li>Work with us</li></ul>
<div class="abs f-head" style="left:196px">SUPPORT</div>
<ul class="abs f-links" style="left:196px"><li>FAQ</li><li>Legal notices</li><li>Cancellation policy</li><li>Terms of use</li><li>Privacy policy</li></ul>
<div class="abs f-head" style="left:320px">QUICK LINKS</div>
<ul class="abs f-links" style="left:320px"><li>Discover Cayman</li><li>Thing to Do</li><li>My Trip Planner</li><li>Map</li><li>Contact Us</li></ul>
<div class="abs f-head" style="left:445px">SIGN UP NEWSLETTER</div>
<div class="abs email">Enter Email</div>
<div class="abs signup">SIGN UP</div>
<div class="abs f-note">Keep up to date as we expand in to new regions</div>
<div class="abs social" style="left:445px;background:#2f5597"></div>
<div class="abs social" style="left:471px;background:#2aa3e6"></div>
<div class="abs social" style="left:496px;background:#1e8fb3"></div>
<div class="abs social" style="left:521px;background:#d6242a"></div>
<div class="abs f-rule"></div>
<div class="abs copy">Copyright © 2019, IsleRoute. All rights reserved &nbsp;|&nbsp; Privacy policy &nbsp;|&nbsp; Terms and conditions</div>

</body>
</html>
```